Velora Crest Expo - a fashion, art, design exhibition

Please see below. The poster must be very elegant. Eventhough it has an african name and feel, it should be modern and elegant so that it attracts all types of backgrounds and races to the show.

I want this poster to be so good that it attracts Sponsors, partners and exhibitors to want to be part of the show. So its my key marketing document.

Size: A0. Good luck and be creative!

Brief is below

The VELORA CREST EXPO 2014

Dates: 19- 21 SEPTEMBER 2014:
all weekend event -open to the public
Time:
9am-5PM
OPEN TO THE PUBLIC
*Fashion shows will have exclusive show times

Venue to be confirmed

SHOWCASING
Fashion designers;
• Shoes designers;
• Accessory designers;
• Art;
• Cosmetics;
• Hair;
• Home and Décor;
• Media;
• Textiles and manufacturing;
• Technology;
• Tourism;
• Luxury/Lifestyle;
• Food & Others.

Countries representing:
SouthAfrica
Nigeria
Ghana
Kenya
Zimbabwe
Tanzania
Uganda
Ethiopia
Botswana
Mozambique
Zambia

To exhibit, partner or sponsor contact us:
Email: info@veloracrestexpo.com
Tele: 073 564 2187
Web: www.theveloracrestexpo.com
Facebook:/theveloracrestexpo
Twitter:@the veloracrestexpo

All rights reserved. Presented by Drembel International

Reason: I have extended the deadline because, one designer asked for it.

Please see the updated brief. I had alot of queries on the brief so i have shortened it.

Hi Designers,

I've attached our logo below. Please use logo version 2.1.3

We are interested in receiving more designs (right now there are only 2 to choose from)
Looking forward to your creativity.

Best regards

Hi all, Thanks for the designs that have been submitted. What i am really looking for is something that is elegant and catchy. The event/expo is an exhibition that will showcase, fashion, art, design, interior, comestics an hair etc. there will also be fashion shows that will be held on that day. It will be a nice classy event, that will draw crowds from all over Africa to participate. I have pasted the link below as a guide. Feel free to amend the brief or just use some of the info that will work. I need more designs. https://www.sample-lookup.example/search?q=example+poster+reference

Target Market(s)

The public/ in SouthA frica, Africa and the world:
-Fashion bloggers
-Magazine Editors
-Fashion Brands
-Industry experts

those who attend will want to see:

- To interact and socialise with entrepreneurs
- See what’s new
- Evaluate products and suppliers
- Keep abreast of industry and market developments
- Network/develop business contacts
Solve specific problems
- Find new markets
- Appoint agents/seek principals
- Discuss specific terms/conditions/pricing
- Consolidate business relationships

It will be an all weekend event. Adults aged 25 as per above

Industry/Entity Type

Marketing

Font styles to use
Serif

Requirements
Must have
• The poster must be elegant and appealing
Nice to have
• Be creative, think, Harbourline Style Days or Corvena style days and exhibition/trade fair combined.

The event will be fashion driven, so that lifestyle brands can also exhibit there
Should not have
• No old style

Not tacky

Must be classy

```html
<!DOCTYPE html>
<html lang="en">
<head>
<meta charset="utf-8">
<title>The Velora Crest Expo 2014</title>
<link rel="stylesheet" href="https://fonts.googleapis.com/css2?family=Playfair+Display+SC:wght@400;700&family=Playfair+Display:wght@400&family=Questrial&display=swap">
<style>
  :root {
    --ink: #141414;
    --copper: #a8673a;
    --paper: #ffffff;
    --muted: #3a3a3a;
    --hair-tone: #b77a4e;
    --runway-tone: #c9c4c8;
    --decor-tone: #b9aca0;
    --art-tone: #d0663a;
  }
  * { box-sizing: border-box; margin: 0; padding: 0; }
  html, body { width: 849px; height: 1200px; overflow: hidden; background: var(--paper); }
  .poster {
    position: relative; width: 849px; height: 1200px; overflow: hidden;
    background: var(--paper); color: var(--ink);
    font-family: "Questrial", "Helvetica Neue", Arial, sans-serif;
  }
  .title-the {
    position: absolute; top: 14px; left: 0; width: 100%; text-align: center;
    font-family: "Questrial", sans-serif; font-size: 58px; letter-spacing: 4px;
    color: var(--copper); line-height: 1;
  }
  .title-name {
    position: absolute; top: 66px; left: 0; width: 100%; text-align: center;
    font-family: "Playfair Display SC", "Bodoni Moda", serif; font-weight: 700;
    font-size: 112px; line-height: 1; letter-spacing: 1px; white-space: nowrap;
  }
  .title-year {
    position: absolute; top: 176px; left: 0; width: 100%; text-align: center;
    font-family: "Playfair Display", serif; font-weight: 400;
    font-size: 118px; line-height: 1; color: var(--copper); white-space: nowrap;
  }
  .gallery { position: absolute; top: 296px; left: 13px; width: 813px; height: 324px; }
  .gallery-tile { position: absolute; top: 0; height: 324px; width: 199px; }
  .tile-hair   { left: 0;   background: linear-gradient(135deg, var(--hair-tone), #6d4128 70%, #5aa0c8); }
  .tile-runway { left: 205px; background: linear-gradient(180deg, #eeeaf0, var(--runway-tone) 60%, #8a7f8c); }
  .tile-decor  { left: 409px; background: linear-gradient(180deg, #cfc5bb, var(--decor-tone) 60%, #8f7a66); }
  .tile-art    { left: 613px; background: linear-gradient(160deg, #e08a3c, var(--art-tone) 45%, #4f8c7a); }
  .date-line {
    position: absolute; top: 636px; left: 0; width: 100%; text-align: center;
    font-size: 57px; line-height: 1; white-space: nowrap;
  }
  .date-line svg { vertical-align: middle; margin: 0 10px; position: relative; top: -6px; }
  .public-line {
    position: absolute; top: 700px; left: 0; width: 100%; text-align: center;
    font-size: 44px; letter-spacing: 3px; line-height: 1;
  }
  .venue-line {
    position: absolute; top: 752px; left: 0; width: 100%; text-align: center;
    font-size: 35px; letter-spacing: 2px; line-height: 1;
  }
  .sector-list {
    position: absolute; top: 795px; font-size: 19.5px; line-height: 21px; list-style: none;
  }
  .sectors-left  { right: 446px; text-align: right; }
  .sectors-right { left: 433px; text-align: left; }
  .contact-call {
    position: absolute; top: 958px; left: 0; width: 100%; text-align: center;
    font-size: 27px; letter-spacing: 0.5px; line-height: 1; white-space: nowrap;
  }
  .brand-mark {
    position: absolute; top: 1034px; left: 128px; width: 280px;
    display: flex; align-items: center; gap: 10px;
    font-family: "Playfair Display", serif; font-size: 30px; color: var(--ink); white-space: nowrap;
  }
  .brand-mark .dot { width: 14px; height: 14px; border-radius: 50%; background: var(--copper); flex: none; }
  .contact-list {
    position: absolute; top: 1000px; left: 435px; list-style: none;
    font-size: 16.5px; line-height: 21.5px; color: var(--muted); letter-spacing: 0.4px;
  }
  .countries {
    position: absolute; top: 1124px; left: 0; width: 100%; text-align: center;
    font-size: 12.5px; color: var(--muted);
  }
  .rights {
    position: absolute; top: 1150px; left: 0; width: 100%; text-align: center;
    font-size: 10px; letter-spacing: 2px; color: var(--muted);
  }
</style>
</head>
<body>
<main class="poster">
  <header>
    <div class="title-the">THE</div>
    <h1 class="title-name">Velora Crest</h1>
    <div class="title-year">EXPO 2014</div>
  </header>

  <section class="gallery">
    <div class="gallery-tile tile-hair" role="img" aria-label="Close-up photo of braided cornrow hairstyle with colourful beads"></div>
    <div class="gallery-tile tile-runway" role="img" aria-label="Photo of models walking a fashion runway"></div>
    <div class="gallery-tile tile-decor" role="img" aria-label="Photo of home decor: wall hooks, shelf ornaments and baskets"></div>
    <div class="gallery-tile tile-art" role="img" aria-label="Colourful painting of women carrying baskets"></div>
  </section>

  <div class="date-line">19-21 SEPTEMBER<svg width="26" height="26" viewBox="0 0 26 26" aria-hidden="true"><circle cx="13" cy="13" r="11.5" fill="none" stroke="var(--copper)" stroke-width="2.5"/><circle cx="13" cy="13" r="6" fill="none" stroke="var(--copper)" stroke-width="2.5"/><circle cx="13" cy="13" r="2" fill="var(--copper)"/></svg>9AM-5PM</div>
  <div class="public-line">OPEN TO THE PUBLIC</div>
  <div class="venue-line">VENUE NAME</div>

  <ul class="sector-list sectors-left">
    <li>Fashion Designers</li><li>Shoes Designers</li><li>Accessory Designers</li><li>Art</li><li>Cosmetics</li><li>Hair</li><li>Home and Décor</li>
  </ul>
  <ul class="sector-list sectors-right">
    <li>Media</li><li>Textiles</li><li>Manufacturing</li><li>Technology</li><li>Tourism</li><li>Luxury and Lifestyle</li><li>Food</li>
  </ul>

  <div class="contact-call">TO EXHIBIT, PARTNER OR SPONSOR, CONTACT US:</div>

  <div class="brand-mark"><span class="dot"></span>Velora Crest Expo</div>

  <ul class="contact-list">
    <li>Email: info@veloracrestexpo.com</li>
    <li>Tele: 073 564 2187</li>
    <li>Web: www.theveloracrestexpo.com</li>
    <li>Facebook: /theveloracrestexpo</li>
    <li>Twitter: @the veloracrestexpo</li>
  </ul>

  <p class="countries">Countries representing: SouthAfrica, Nigeria, Ghana, Kenya, Zimbabwe, Tanzania, Uganda, Ethiopia, Botswana, Mozambique, Zambia</p>
  <p class="rights">ALL RIGHTS RESERVED. PRESENTED BY DREMBEL INTERNATIONAL</p>
</main>
</body>
</html>
```